New website for concierge mobile medical service

new website for business:
WEBSITE REQUEST LIST:
Luxury product look.
Professional. Clean & simple, NO stock people photos. Graphics OK.
Black and white text.

```html
<!DOCTYPE html>
<html lang="en">
<head>
<meta charset="utf-8">
<title>Vesta — Medications Dispensed</title>
<link href="https://fonts.googleapis.com/css2?family=Lato:wght@400;700;900&display=swap" rel="stylesheet">
<style>
:root{
  --ink:#222;
  --muted:#555;
  --teal:#1c8a98;
  --teal-dark:#116777;
  --navy:#07141f;
  --navy-2:#0c2a38;
  --white:#fff;
  --line:#cfd6da;
  --footer:#1b1b1b;
}
*{box-sizing:border-box;margin:0;padding:0}
html,body{width:763px;height:1200px;overflow:hidden;background:var(--white);font-family:'Lato',sans-serif;color:var(--ink)}
.page{position:relative;width:763px;height:1200px}

.site-header{position:absolute;top:0;left:0;width:100%;height:46px;background:var(--white)}
.brand{position:absolute;left:36px;top:6px;display:flex;align-items:center;gap:8px}
.brand-mark{width:34px;height:34px;border-radius:50%;background:var(--navy-2);border:3px solid var(--teal)}
.brand-name{font-weight:900;font-size:17px;color:var(--navy-2)}
.phone{position:absolute;right:40px;top:6px;font-size:10px;font-weight:700;color:var(--navy-2);display:flex;align-items:center;gap:6px}
.phone-icon{width:15px;height:15px;background:var(--teal);border-radius:3px;display:flex;align-items:center;justify-content:center}
.main-nav{position:absolute;right:40px;top:27px;display:flex;gap:14px;font-size:7.5px;font-weight:700;letter-spacing:.3px;color:var(--ink)}

.hero{position:absolute;top:46px;left:0;width:100%;height:196px;background:radial-gradient(circle at 85% 50%,#153e52 0%,var(--navy-2) 30%,var(--navy) 75%)}
.hero-title{position:absolute;left:36px;top:40px;font-size:26px;font-weight:900;color:var(--white)}
.hero-badge{position:absolute;left:618px;top:42px}

.intro{position:absolute;left:51px;top:258px;font-size:8.5px;color:var(--muted)}
.conditions{position:absolute;top:286px;list-style:none;font-size:8.5px;color:var(--ink)}
.conditions li{height:23.5px;display:flex;align-items:center;gap:8px}
.conditions svg{flex:none}
.col-1{left:51px}.col-2{left:381px}.col-3{left:609px}

.subscribe{position:absolute;top:812px;left:0;width:100%;height:143px;background:linear-gradient(180deg,var(--teal) 0%,var(--teal-dark) 100%);text-align:center}
.subscribe h2{margin-top:24px;font-size:22px;font-weight:700;color:var(--white)}
.sub-fields{position:absolute;top:68px;left:173px;display:flex;gap:10px}
.field{background:var(--white);border:1px solid var(--line);height:18px;font-size:6.5px;color:#777;padding:5px 6px;text-align:left}
.sub-fields .field{width:203px}
.btn{position:absolute;background:var(--teal);border:1px solid rgba(255,255,255,.6);color:var(--white);font-size:7px;font-weight:700;letter-spacing:.5px;display:flex;align-items:center;justify-content:center}
.subscribe .btn{top:95px;left:173px;width:416px;height:18px;background:rgba(255,255,255,.15)}

.contact{position:absolute;top:955px;left:0;width:100%;height:163px;text-align:center}
.contact h2{margin-top:12px;font-size:22px;font-weight:700;color:var(--ink)}
.contact p{margin-top:4px;font-size:8.5px;color:var(--muted)}
.contact .field{position:absolute;width:228px}
.contact .message{width:466px;height:30px}
.contact .btn{top:140px;left:297px;width:170px;height:16px;border:none;background:var(--teal)}

.site-footer{position:absolute;top:1118px;left:0;width:100%;height:82px;background:var(--footer);text-align:center;color:var(--white)}
.footer-nav{display:flex;justify-content:center;gap:22px;margin-top:12px;font-size:7.5px;font-weight:700}
.social{display:flex;justify-content:center;gap:8px;margin-top:14px}
.social span{width:12px;height:12px;border-radius:50%;background:#bbb}
.copyright{margin-top:9px;font-size:6.5px;color:#aaa}
</style>
</head>
<body>
<div class="page">
  <header class="site-header">
    <div class="brand"><span class="brand-mark"></span><span class="brand-name">Vesta</span></div>
    <div class="phone"><span class="phone-icon"><svg width="9" height="9" viewBox="0 0 24 24"><path fill="#fff" d="M6.6 10.8a15 15 0 0 0 6.6 6.6l2.2-2.2c.3-.3.7-.4 1-.2 1.1.4 2.3.6 3.6.6.6 0 1 .4 1 1V20c0 .6-.4 1-1 1A17 17 0 0 1 3 4c0-.6.4-1 1-1h3.5c.6 0 1 .4 1 1 0 1.3.2 2.5.6 3.6.1.3 0 .7-.2 1z"/></svg></span>555-014-0199</div>
    <nav class="main-nav"><span>HOME</span><span>ABOUT US</span><span>WHY VESTA?</span><span>SERVICE AREA</span><span>OTHER</span><span>FAQ</span><span>CONTACT US</span></nav>
  </header>

  <section class="hero">
    <h1 class="hero-title">Medications Dispensed</h1>
    <svg class="hero-badge" width="104" height="104" viewBox="0 0 104 104" role="img" aria-label="Mobile medical vehicle icon">
      <circle cx="52" cy="52" r="50" fill="none" stroke="#2aa9bb" stroke-opacity=".35" stroke-width="2"/>
      <circle cx="52" cy="52" r="40" fill="#0e3344" stroke="#2aa9bb" stroke-width="1.5"/>
      <rect x="36" y="50" width="32" height="14" rx="3" fill="none" stroke="#fff" stroke-width="2"/>
      <circle cx="43" cy="66" r="3" fill="#fff"/><circle cx="61" cy="66" r="3" fill="#fff"/>
      <rect x="49" y="42" width="6" height="8" fill="#fff"/>
    </svg>
  </section>

  <p class="intro">We are experienced in treating these conditions and all of these can be treated in the home.</p>

  <ul class="conditions col-1">
    <li><svg width="9" height="9" viewBox="0 0 10 10"><rect width="10" height="10" fill="#1c8a98"/><path d="M2 5l2 2 4-4" stroke="#fff" stroke-width="1.5" fill="none"/></svg>Anxiety</li>
    <li><svg width="9" height="9" viewBox="0 0 10 10"><rect width="10" height="10" fill="#1c8a98"/><path d="M2 5l2 2 4-4" stroke="#fff" stroke-width="1.5" fill="none"/></svg>Asthma attacks</li>
    <li><svg width="9" height="9" viewBox="0 0 10 10"><rect width="10" height="10" fill="#1c8a98"/><path d="M2 5l2 2 4-4" stroke="#fff" stroke-width="1.5" fill="none"/></svg>Back Pain</li>
    <li><svg width="9" height="9" viewBox="0 0 10 10"><rect width="10" height="10" fill="#1c8a98"/><path d="M2 5l2 2 4-4" stroke="#fff" stroke-width="1.5" fill="none"/></svg>Bed sores</li>
    <li><svg width="9" height="9" viewBox="0 0 10 10"><rect width="10" height="10" fill="#1c8a98"/><path d="M2 5l2 2 4-4" stroke="#fff" stroke-width="1.5" fill="none"/></svg>Boils and abscesses</li>
    <li><svg width="9" height="9" viewBox="0 0 10 10"><rect width="10" height="10" fill="#1c8a98"/><path d="M2 5l2 2 4-4" stroke="#fff" stroke-width="1.5" fill="none"/></svg>Bronchitis and Chest congestion</li>
    <li><svg width="9" height="9" viewBox="0 0 10 10"><rect width="10" height="10" fill="#1c8a98"/><path d="M2 5l2 2 4-4" stroke="#fff" stroke-width="1.5" fill="none"/></svg>Catheter services</li>
    <li><svg width="9" height="9" viewBox="0 0 10 10"><rect width="10" height="10" fill="#1c8a98"/><path d="M2 5l2 2 4-4" stroke="#fff" stroke-width="1.5" fill="none"/></svg>Crohn's disease</li>
    <li><svg width="9" height="9" viewBox="0 0 10 10"><rect width="10" height="10" fill="#1c8a98"/><path d="M2 5l2 2 4-4" stroke="#fff" stroke-width="1.5" fill="none"/></svg>Congestive heart failure (CHF)</li>
    <li><svg width="9" height="9" viewBox="0 0 10 10"><rect width="10" height="10" fill="#1c8a98"/><path d="M2 5l2 2 4-4" stroke="#fff" stroke-width="1.5" fill="none"/></svg>Constipation (severe)</li>
    <li><svg width="9" height="9" viewBox="0 0 10 10"><rect width="10" height="10" fill="#1c8a98"/><path d="M2 5l2 2 4-4" stroke="#fff" stroke-width="1.5" fill="none"/></svg>Cough &amp; Croup (severe)</li>
    <li><svg width="9" height="9" viewBox="0 0 10 10"><rect width="10" height="10" fill="#1c8a98"/><path d="M2 5l2 2 4-4" stroke="#fff" stroke-width="1.5" fill="none"/></svg>COPD symptoms</li>
    <li><svg width="9" height="9" viewBox="0 0 10 10"><rect width="10" height="10" fill="#1c8a98"/><path d="M2 5l2 2 4-4" stroke="#fff" stroke-width="1.5" fill="none"/></svg>Cuts &amp; lacerations requiring stitches</li>
    <li><svg width="9" height="9" viewBox="0 0 10 10"><rect width="10" height="10" fill="#1c8a98"/><path d="M2 5l2 2 4-4" stroke="#fff" stroke-width="1.5" fill="none"/></svg>Dehydration</li>
    <li><svg width="9" height="9" viewBox="0 0 10 10"><rect width="10" height="10" fill="#1c8a98"/><path d="M2 5l2 2 4-4" stroke="#fff" stroke-width="1.5" fill="none"/></svg>Diarrhea</li>
    <li><svg width="9" height="9" viewBox="0 0 10 10"><rect width="10" height="10" fill="#1c8a98"/><path d="M2 5l2 2 4-4" stroke="#fff" stroke-width="1.5" fill="none"/></svg>Diverticulitis</li>
    <li><svg width="9" height="9" viewBox="0 0 10 10"><rect width="10" height="10" fill="#1c8a98"/><path d="M2 5l2 2 4-4" stroke="#fff" stroke-width="1.5" fill="none"/></svg>Dizziness &amp; motion sickness</li>
    <li><svg width="9" height="9" viewBox="0 0 10 10"><rect width="10" height="10" fill="#1c8a98"/><path d="M2 5l2 2 4-4" stroke="#fff" stroke-width="1.5" fill="none"/></svg>Ear infections</li>
  </ul>

  <ul class="conditions col-2">
    <li><svg width="9" height="9" viewBox="0 0 10 10"><rect width="10" height="10" fill="#1c8a98"/><path d="M2 5l2 2 4-4" stroke="#fff" stroke-width="1.5" fill="none"/></svg>Edema &amp; swelling (fluid buildup)</li>
    <li><svg width="9" height="9" viewBox="0 0 10 10"><rect width="10" height="10" fill="#1c8a98"/><path d="M2 5l2 2 4-4" stroke="#fff" stroke-width="1.5" fill="none"/></svg>Eye infections &amp; eye injuries</li>
    <li><svg width="9" height="9" viewBox="0 0 10 10"><rect width="10" height="10" fill="#1c8a98"/><path d="M2 5l2 2 4-4" stroke="#fff" stroke-width="1.5" fill="none"/></svg>Fever</li>
    <li><svg width="9" height="9" viewBox="0 0 10 10"><rect width="10" height="10" fill="#1c8a98"/><path d="M2 5l2 2 4-4" stroke="#fff" stroke-width="1.5" fill="none"/></svg>Flu (influenza)</li>
    <li><svg width="9" height="9" viewBox="0 0 10 10"><rect width="10" height="10" fill="#1c8a98"/><path d="M2 5l2 2 4-4" stroke="#fff" stroke-width="1.5" fill="none"/></svg>Food poisoning</li>
    <li><svg width="9" height="9" viewBox="0 0 10 10"><rect width="10" height="10" fill="#1c8a98"/><path d="M2 5l2 2 4-4" stroke="#fff" stroke-width="1.5" fill="none"/></svg>Fractures Sprains, Strains, Bruises</li>
    <li><svg width="9" height="9" viewBox="0 0 10 10"><rect width="10" height="10" fill="#1c8a98"/><path d="M2 5l2 2 4-4" stroke="#fff" stroke-width="1.5" fill="none"/></svg>Head injuries</li>
    <li><svg width="9" height="9" viewBox="0 0 10 10"><rect width="10" height="10" fill="#1c8a98"/><path d="M2 5l2 2 4-4" stroke="#fff" stroke-width="1.5" fill="none"/></svg>Heart palpitations</li>
    <li><svg width="9" height="9" viewBox="0 0 10 10"><rect width="10" height="10" fill="#1c8a98"/><path d="M2 5l2 2 4-4" stroke="#fff" stroke-width="1.5" fill="none"/></svg>Infections – wounds, skin, sinus</li>
    <li><svg width="9" height="9" viewBox="0 0 10 10"><rect width="10" height="10" fill="#1c8a98"/><path d="M2 5l2 2 4-4" stroke="#fff" stroke-width="1.5" fill="none"/></svg>Kidney stones</li>
    <li><svg width="9" height="9" viewBox="0 0 10 10"><rect width="10" height="10" fill="#1c8a98"/><path d="M2 5l2 2 4-4" stroke="#fff" stroke-width="1.5" fill="none"/></svg>Migraines</li>
    <li><svg width="9" height="9" viewBox="0 0 10 10"><rect width="10" height="10" fill="#1c8a98"/><path d="M2 5l2 2 4-4" stroke="#fff" stroke-width="1.5" fill="none"/></svg>Nosebleeds</li>
    <li><svg width="9" height="9" viewBox="0 0 10 10"><rect width="10" height="10" fill="#1c8a98"/><path d="M2 5l2 2 4-4" stroke="#fff" stroke-width="1.5" fill="none"/></svg>Pregnancy tests</li>
    <li><svg width="9" height="9" viewBox="0 0 10 10"><rect width="10" height="10" fill="#1c8a98"/><path d="M2 5l2 2 4-4" stroke="#fff" stroke-width="1.5" fill="none"/></svg>Pneumonia</li>
    <li><svg width="9" height="9" viewBox="0 0 10 10"><rect width="10" height="10" fill="#1c8a98"/><path d="M2 5l2 2 4-4" stroke="#fff" stroke-width="1.5" fill="none"/></svg>Rashes</li>
    <li><svg width="9" height="9" viewBox="0 0 10 10"><rect width="10" height="10" fill="#1c8a98"/><path d="M2 5l2 2 4-4" stroke="#fff" stroke-width="1.5" fill="none"/></svg>Respiratory infections</li>
    <li><svg width="9" height="9" viewBox="0 0 10 10"><rect width="10" height="10" fill="#1c8a98"/><path d="M2 5l2 2 4-4" stroke="#fff" stroke-width="1.5" fill="none"/></svg>Severe scrapes &amp; abrasions</li>
    <li><svg width="9" height="9" viewBox="0 0 10 10"><rect width="10" height="10" fill="#1c8a98"/><path d="M2 5l2 2 4-4" stroke="#fff" stroke-width="1.5" fill="none"/></svg>Shingles</li>
  </ul>

  <ul class="conditions col-3">
    <li><svg width="9" height="9" viewBox="0 0 10 10"><rect width="10" height="10" fill="#1c8a98"/><path d="M2 5l2 2 4-4" stroke="#fff" stroke-width="1.5" fill="none"/></svg>Shortness of breath</li>
    <li><svg width="9" height="9" viewBox="0 0 10 10"><rect width="10" height="10" fill="#1c8a98"/><path d="M2 5l2 2 4-4" stroke="#fff" stroke-width="1.5" fill="none"/></svg>Sinus infections</li>
    <li><svg width="9" height="9" viewBox="0 0 10 10"><rect width="10" height="10" fill="#1c8a98"/><path d="M2 5l2 2 4-4" stroke="#fff" stroke-width="1.5" fill="none"/></svg>Strep throat</li>
    <li><svg width="9" height="9" viewBox="0 0 10 10"><rect width="10" height="10" fill="#1c8a98"/><path d="M2 5l2 2 4-4" stroke="#fff" stroke-width="1.5" fill="none"/></svg>Splinting</li>
    <li><svg width="9" height="9" viewBox="0 0 10 10"><rect width="10" height="10" fill="#1c8a98"/><path d="M2 5l2 2 4-4" stroke="#fff" stroke-width="1.5" fill="none"/></svg>Urinary tract infections (UTIs)</li>
    <li><svg width="9" height="9" viewBox="0 0 10 10"><rect width="10" height="10" fill="#1c8a98"/><path d="M2 5l2 2 4-4" stroke="#fff" stroke-width="1.5" fill="none"/></svg>Urination issues</li>
    <li><svg width="9" height="9" viewBox="0 0 10 10"><rect width="10" height="10" fill="#1c8a98"/><path d="M2 5l2 2 4-4" stroke="#fff" stroke-width="1.5" fill="none"/></svg>Vertigo</li>
    <li><svg width="9" height="9" viewBox="0 0 10 10"><rect width="10" height="10" fill="#1c8a98"/><path d="M2 5l2 2 4-4" stroke="#fff" stroke-width="1.5" fill="none"/></svg>Viral infections</li>
    <li><svg width="9" height="9" viewBox="0 0 10 10"><rect width="10" height="10" fill="#1c8a98"/><path d="M2 5l2 2 4-4" stroke="#fff" stroke-width="1.5" fill="none"/></svg>Vomiting (severe)</li>
    <li><svg width="9" height="9" viewBox="0 0 10 10"><rect width="10" height="10" fill="#1c8a98"/><path d="M2 5l2 2 4-4" stroke="#fff" stroke-width="1.5" fill="none"/></svg>Weakness and Fatigue</li>
    <li><svg width="9" height="9" viewBox="0 0 10 10"><rect width="10" height="10" fill="#1c8a98"/><path d="M2 5l2 2 4-4" stroke="#fff" stroke-width="1.5" fill="none"/></svg>Wounds</li>
  </ul>

  <section class="subscribe">
    <h2>Subscribe</h2>
    <div class="sub-fields"><div class="field">Enter Name</div><div class="field">Enter Email Address</div></div>
    <div class="btn">SUBSCRIBE NOW</div>
  </section>

  <section class="contact">
    <h2>Contact Us</h2>
    <p>We want to hear from you! Click below to send us a message and receive upcoming information.</p>
    <div class="field" style="top:58px;left:150px">Full Name</div>
    <div class="field" style="top:58px;left:388px">Enter Email Address</div>
    <div class="field" style="top:82px;left:150px">Phone No</div>
    <div class="field" style="top:82px;left:388px">Subject</div>
    <div class="field message" style="top:106px;left:150px">Message</div>
    <div class="btn">SUBMIT NOW</div>
  </section>

  <footer class="site-footer">
    <nav class="footer-nav"><span>HOME</span><span>ABOUT US</span><span>WHY VESTA?</span><span>SERVICE AREA</span><span>OTHER</span><span>CONTACT US</span></nav>
    <div class="social"><span></span><span></span><span></span><span></span><span></span></div>
    <p class="copyright">Copyright © 2019. Company Name. All rights reserved.</p>
  </footer>
</div>
</body>
</html>
```